Harborline Toma's Chinese/Dim Sum Restaurant Menu

Harborline Toma's is a seafood-asian fusion restaurant featuring dim sum and other classical asian fusion items.

We need a menu design that includes both our food menu and our drink menu.

Food menu: Needs to have space for descriptions of food (please just include a place holder and we will input them later). See attached for food menu items.

Drink menu: Just lists of items with prices. See attached Jade Lantern Menu- please include the same items, but rebrand for Harborline Toma's.

The menus must be able to be printed in a 4.25x11in paper.

We want something modern and contemporary. My boss likes geometrical design aspects and minimalism. So, nothing too ornate. But, it has to be different from the Jade Lantern menus. Colors can be black, red, gold or blue- but it must be able to be tied into our black and red Harborline Toma's logo. Including elements of Chinese culture, especially fishing, is a plus, but not necessary.

We also need this in ai format when we download final copy so we can edit in the future.

UPDATE: Please note, we already have a logo.

Target Market(s)

Upscale family diners

Industry/Entity Type

Chinese Food

Font styles to use
Serif
Sans Serif

Colors
0054AA
0677BA
7BADD7
CADEEF
E8F1F8
0094D4
00A9DD
6FCCEA
C7EBF8
E9F6FB
FFC000
F8CF3A
FAE287
FDF2CF
FEFAEE
EB3D1F
EC4F4E
F09395
F8D3D4
FCEDEE

Requirements
Must have
• Classic, minimalist, elegant

```html
<!DOCTYPE html>
<html lang="en">
<head>
<meta charset="utf-8">
<title>Harborline Toma's — Food &amp; Drink Menu</title>
<link rel="stylesheet" href="https://fonts.googleapis.com/css2?family=Oswald:wght@400;500;700&family=Roboto+Condensed:wght@400;700&family=Playfair+Display:wght@700&display=swap">
<style>
:root{
  --red:#EB3D1F;
  --red-soft:#EC4F4E;
  --ink:#161616;
  --grey:#6b6b6b;
  --paper:#f5f5f3;
  --paper-edge:#e9e9e6;
  --stage:#ffffff;
  --gold:#FFC000;
  --lemon:#F8CF3A;
}
*{box-sizing:border-box;margin:0;padding:0}
html,body{width:739px;height:1200px;overflow:hidden;background:var(--stage)}
body{position:relative;font-family:"Roboto Condensed",Arial,sans-serif;color:var(--ink)}
.panel{position:absolute;background:linear-gradient(180deg,var(--paper),var(--paper-edge));box-shadow:0 2px 6px rgba(0,0,0,.18);overflow:hidden}
.panel--cover{left:12px;top:12px;width:222px;height:575px}
.panel--food{left:259px;top:12px;width:222px;height:575px}
.panel--more{left:505px;top:12px;width:222px;height:575px}
.panel--wine{left:135px;top:605px;width:232px;height:583px}
.panel--liquor{left:372px;top:605px;width:232px;height:583px}
.abs{position:absolute}
.brand{display:flex;align-items:center;gap:4px;font-family:"Oswald",sans-serif;font-weight:700;color:var(--ink);letter-spacing:.5px;text-transform:uppercase}
.brand__dot{width:9px;height:9px;border-radius:50%;background:var(--red)}
.photo{position:absolute;border-radius:50%}
.photo--dish{background:radial-gradient(circle at 45% 40%,#d9743a 0 30%,#8a3a1c 55%,#1d1a18 72%)}
.photo--green{background:radial-gradient(circle at 45% 40%,#8cae4a 0 30%,#3e5a22 58%,#1b1c18 74%)}
.photo--soup{background:radial-gradient(circle at 50% 45%,#d6472a 0 40%,#7a1f12 62%,#1b1a19 76%)}
.photo--noodle{background:radial-gradient(circle at 50% 45%,#d8a24e 0 38%,#8a5a22 60%,#1e1b18 76%)}
.photo--sweet{background:radial-gradient(circle at 50% 45%,#e8d6b8 0 35%,#a3422c 55%,#1e1b18 74%)}
.section-title{position:absolute;font-family:"Oswald",sans-serif;font-weight:700;font-size:15px;line-height:1;text-transform:uppercase;color:var(--ink)}
.section-title--red{color:var(--red)}
.items{position:absolute;list-style:none;font-size:5.6px;line-height:7.6px;color:#333}
.items li{display:flex;justify-content:space-between;gap:4px}
.items b{font-weight:700;color:var(--ink)}
.tags li b{background:var(--ink);color:#fff;border-radius:3px;padding:0 3px;margin-left:2px;font-size:5px}
.tags li{margin-bottom:1.2px}
.tags li span:first-child{flex:1}
</style>
</head>
<body>

<!-- Cover -->
<section class="panel panel--cover">
  <div class="brand abs" style="left:0;right:0;top:22px;justify-content:center;font-size:15px"><span class="brand__dot"></span>Harborline Toma's</div>
  <div class="abs" style="left:20px;top:62px;font-family:'Oswald',sans-serif;font-weight:700;font-size:27px;line-height:1;color:var(--red)">FOOD <span style="color:var(--ink)">&amp;</span> DRINK</div>
  <div class="abs" style="left:18px;top:88px;font-family:'Oswald',sans-serif;font-weight:700;font-size:62px;line-height:1;color:var(--ink)">MENU</div>
  <div class="photo" role="img" aria-label="Lemon slice" style="left:168px;top:150px;width:38px;height:38px;background:radial-gradient(circle,#fbe79a 0 50%,var(--lemon) 75%,#e0b020)"></div>
  <div class="photo photo--dish" role="img" aria-label="Penne pasta dish on a dark plate" style="left:18px;top:172px;width:160px;height:160px"></div>
  <div class="abs" style="left:150px;top:262px;width:30px;height:30px;border-radius:50%;background:var(--gold);color:#fff;font-family:'Oswald',sans-serif;font-weight:700;font-size:13px;display:flex;align-items:center;justify-content:center">$5</div>
  <div class="abs" style="left:14px;top:342px;width:84px;height:84px;border-radius:50%;background:var(--red);color:#fff;text-align:center;font-family:'Oswald',sans-serif;padding-top:16px">
    <div style="font-size:11px;font-weight:700;line-height:1.05">HAPPY HOUR<br><span style="color:var(--gold)">APPETIZERS</span></div>
    <div style="font-size:6px;margin-top:3px">AVAILABLE</div>
    <div style="font-size:7px;font-weight:500">3PM – 6PM</div>
  </div>
  <div class="abs" style="left:118px;top:352px;font-family:'Oswald',sans-serif;font-weight:700;font-size:15px;line-height:1.05;color:var(--red)">DRINK <span style="color:var(--ink)">&amp;</span><br><span style="color:var(--ink)">APPETIZERS</span></div>
  <div class="abs" style="left:30px;top:448px;font-family:'Oswald',sans-serif;font-weight:700;font-size:12px;color:var(--red)">$1 OFF <span style="color:var(--ink)">ALL ALCOHOLIC BEVERAGES</span></div>
  <p class="abs" style="left:22px;right:22px;top:478px;font-size:5.4px;line-height:7.2px;color:var(--grey);text-align:center">Consuming raw or undercooked seafood, shellfish or eggs may increase your risk of foodborne illness. Please let your server know about any allergies before ordering. A gratuity may be added for parties of six or more guests.</p>
</section>

<!-- Dim sum & mains -->
<section class="panel panel--food">
  <div class="brand abs" style="left:14px;top:16px;font-size:9px"><span class="brand__dot"></span>Harborline Toma's</div>
  <ul class="items" style="left:150px;top:12px;width:58px;font-size:5.2px;line-height:7px;font-weight:700">
    <li><span>TABLE</span><span>____</span></li><li><span>NAME</span><span>____</span></li><li><span>SERVER</span><span>____</span></li><li><span>GUEST</span><span>____</span></li>
  </ul>

  <h2 class="section-title" style="left:14px;top:52px">Dim Sum</h2>
  <ul class="items" style="left:14px;top:72px;width:118px">
    <li><span>Har Gow</span><b>6</b></li><li><span>Siu Mai</span><b>6</b></li><li><span>Char Siu Bao</span><b>5</b></li><li><span>Turnip Cake</span><b>5</b></li><li><span>Shrimp Rolls</span><b>7</b></li><li><span>Pork Dumplings</span><b>6</b></li><li><span>Crystal Dumplings</span><b>7</b></li><li><span>Egg Tarts</span><b>4</b></li><li><span>Lotus Rice</span><b>6</b></li><li><span>Chive Cakes</span><b>5</b></li>
  </ul>
  <div class="photo photo--dish" role="img" aria-label="Bamboo basket of dumplings" style="left:146px;top:66px;width:62px;height:62px"></div>

  <h2 class="section-title section-title--red" style="left:14px;top:162px">Soup</h2>
  <ul class="items" style="left:14px;top:182px;width:118px">
    <li><span>Wonton Soup</span><b>8</b></li><li><span>Hot &amp; Sour</span><b>7</b></li><li><span>Egg Drop</span><b>6</b></li><li><span>Seafood Tofu</span><b>9</b></li><li><span>Crab Corn</span><b>9</b></li>
  </ul>
  <div class="photo photo--soup" role="img" aria-label="Bowl of red soup" style="left:146px;top:158px;width:62px;height:62px"></div>

  <h2 class="section-title section-title--red" style="left:14px;top:242px">Appetizers</h2>
  <ul class="items" style="left:14px;top:262px;width:118px">
    <li><span>Spring Rolls</span><b>6</b></li><li><span>Crab Rangoon</span><b>8</b></li><li><span>Salt Pepper Squid</span><b>11</b></li><li><span>Pot Stickers</span><b>8</b></li><li><span>Scallion Pancake</span><b>7</b></li><li><span>Chicken Wings</span><b>10</b></li><li><span>Fried Shrimp</span><b>11</b></li><li><span>Edamame</span><b>5</b></li>
  </ul>
  <div class="photo photo--green" role="img" aria-label="Plate of appetizers" style="left:146px;top:250px;width:62px;height:62px"></div>

  <h2 class="section-title section-title--red" style="left:14px;top:348px">Sauteed</h2>
  <ul class="items" style="left:14px;top:368px;width:118px">
    <li><span>Kung Pao Shrimp</span><b>16</b></li><li><span>Black Bean Fish</span><b>18</b></li><li><span>Ginger Scallop</span><b>19</b></li><li><span>Garlic Clams</span><b>17</b></li><li><span>Orange Chicken</span><b>14</b></li><li><span>Mongolian Beef</span><b>16</b></li><li><span>Honey Walnut Shrimp</span><b>18</b></li><li><span>Sweet Sour Pork</span><b>14</b></li>
  </ul>
  <div class="photo photo--dish" role="img" aria-label="Sauteed seafood with vegetables" style="left:146px;top:358px;width:62px;height:62px"></div>

  <div class="abs" style="left:14px;right:14px;bottom:16px;display:flex;justify-content:space-between;font-size:5.4px;color:var(--grey)">
    <span><svg width="6" height="6" viewBox="0 0 6 6"><circle cx="3" cy="3" r="3" fill="#EB3D1F"/></svg> Spicy</span>
    <span><svg width="6" height="6" viewBox="0 0 6 6"><circle cx="3" cy="3" r="3" fill="#4a8a2a"/></svg> Vegetarian</span>
    <span><svg width="6" height="6" viewBox="0 0 6 6"><circle cx="3" cy="3" r="3" fill="#161616"/></svg> Gluten Free</span>
  </div>
</section>

<!-- Veggie, rice, sweets, drinks -->
<section class="panel panel--more">
  <h2 class="section-title" style="left:14px;top:18px">Veggie</h2>
  <ul class="items" style="left:14px;top:38px;width:118px">
    <li><span>Garlic Greens</span><b>11</b></li><li><span>Mapo Tofu</span><b>12</b></li><li><span>Dry Green Beans</span><b>11</b></li><li><span>Eggplant</span><b>12</b></li><li><span>Buddha Delight</span><b>12</b></li><li><span>Bok Choy</span><b>10</b></li>
  </ul>
  <div class="photo photo--green" role="img" aria-label="Stir-fried vegetables" style="left:150px;top:16px;width:58px;height:58px"></div>

  <h2 class="section-title section-title--red" style="left:14px;top:100px">Rice &amp; Noodles</h2>
  <ul class="items" style="left:14px;top:120px;width:118px">
    <li><span>Fried Rice</span><b>11</b></li><li><span>Chow Fun</span><b>13</b></li><li><span>Lo Mein</span><b>12</b></li><li><span>Singapore Noodles</span><b>13</b></li><li><span>Crispy Noodles</span><b>14</b></li><li><span>Yang Chow Rice</span><b>12</b></li><li><span>Seafood Pan</span><b>16</b></li>
  </ul>
  <div class="photo photo--noodle" role="img" aria-label="Bowl of noodles" style="left:150px;top:104px;width:58px;height:58px"></div>

  <h2 class="section-title section-title--red" style="left:14px;top:188px">Sweets &amp; Dessert</h2>
  <ul class="items" style="left:14px;top:208px;width:118px">
    <li><span>Mango Pudding</span><b>6</b></li><li><span>Sesame Balls</span><b>6</b></li><li><span>Egg Custard</span><b>5</b></li><li><span>Red Bean</span><b>5</b></li>
  </ul>
  <div class="photo photo--sweet" role="img" aria-label="Plated dessert" style="left:150px;top:186px;width:52px;height:52px"></div>

  <h2 class="section-title section-title--red" style="left:14px;top:252px">Desserts</h2>
  <ul class="items" style="left:14px;top:272px;width:118px">
    <li><span>Lychee Sorbet</span><b>6</b></li><li><span>Green Tea Ice</span><b>6</b></li><li><span>Fried Banana</span><b>7</b></li><li><span>Almond Jelly</span><b>5</b></li>
  </ul>
  <div class="photo photo--sweet" role="img" aria-label="Dessert bowl" style="left:156px;top:250px;width:46px;height:46px"></div>

  <div class="abs" style="left:14px;top:316px;font-family:'Oswald',sans-serif;font-weight:700;font-size:38px;line-height:1">DRINKS</div>
  <div class="abs" style="left:15px;top:358px;font-family:'Oswald',sans-serif;font-weight:700;font-size:11px;color:var(--red)">NA BEVERAGES</div>
  <ul class="items" style="left:14px;top:376px;width:70px">
    <li><span>Jasmine Tea</span><b>3</b></li><li><span>Oolong Tea</span><b>3</b></li><li><span>Thai Iced Tea</span><b>5</b></li><li><span>Lemonade</span><b>4</b></li><li><span>Soda</span><b>3</b></li><li><span>Ginger Ale</span><b>3</b></li><li><span>Coconut Water</span><b>4</b></li><li><span>Sparkling Water</span><b>4</b></li>
  </ul>
  <div class="abs" role="img" aria-label="Glasses of iced lemonade with lemons" style="left:94px;top:376px;width:128px;height:120px;background:linear-gradient(160deg,#fdf2cf,#f8cf3a 55%,#b88a2a)"></div>
  <div class="abs" role="img" aria-label="Lemons on a wooden board" style="left:0;top:500px;width:222px;height:75px;background:linear-gradient(180deg,#f3e3b0,#c99a55)"></div>
</section>

<!-- Wine & sake -->
<section class="panel panel--wine">
  <h2 class="section-title section-title--red" style="left:16px;top:22px;font-size:18px">Wine</h2>
  <div class="abs" style="left:58px;top:29px;font-size:5.4px;font-weight:700">BOTTLE / GLASS</div>
  <ul class="items tags" style="left:16px;top:48px;width:112px">
    <li><span>House Red</span><b>28</b><b>8</b></li><li><span>House White</span><b>28</b><b>8</b></li><li><span>Pinot Noir</span><b>36</b><b>10</b></li><li><span>Cabernet</span><b>38</b><b>11</b></li><li><span>Merlot</span><b>34</b><b>10</b></li><li><span>Chardonnay</span><b>34</b><b>10</b></li><li><span>Sauvignon Blanc</span><b>32</b><b>9</b></li><li><span>Riesling</span><b>30</b><b>9</b></li>
  </ul>
  <div class="abs" role="img" aria-label="Glass of red wine" style="left:136px;top:14px;width:86px;height:150px;background:radial-gradient(ellipse at 50% 55%,#8a1626 0 28%,#e4e4e2 62%)"></div>
  <div class="abs" role="img" aria-label="Bottle of red wine" style="left:24px;top:190px;width:34px;height:140px;border-radius:10px 10px 4px 4px;background:linear-gradient(90deg,#1a1a1a,#3a1418 50%,#111)"></div>
  <ul class="items tags" style="left:90px;top:200px;width:124px">
    <li><span>Prosecco</span><b>32</b><b>9</b></li><li><span>Rosé</span><b>30</b><b>9</b></li><li><span>Malbec</span><b>34</b><b>10</b></li><li><span>Zinfandel</span><b>32</b><b>9</b></li><li><span>Moscato</span><b>28</b><b>8</b></li><li><span>Pinot Grigio</span><b>30</b><b>9</b></li>
  </ul>
  <h2 class="section-title section-title--red" style="left:16px;top:370px;font-size:18px">Sake</h2>
  <ul class="items tags" style="left:16px;top:396px;width:112px">
    <li><span>House Sake</span><b>12</b></li><li><span>Junmai</span><b>16</b></li><li><span>Nigori</span><b>14</b></li><li><span>Plum Wine</span><b>10</b></li>
  </ul>
  <div class="abs" role="img" aria-label="Cocktail glass with garnish" style="left:140px;top:372px;width:74px;height:80px;background:radial-gradient(ellipse at 50% 45%,#fdf7ea 0 35%,#e2e2df 70%)"></div>
  <div class="abs" role="img" aria-label="Bar tools and bottles" style="left:0;top:470px;width:232px;height:113px;background:linear-gradient(180deg,#e6e6e3,#a9a39a 60%,#5b4a3a)"></div>
</section>

<!-- Liquor & cocktails -->
<section class="panel panel--liquor">
  <h2 class="section-title section-title--red" style="left:16px;top:20px;font-size:18px">Liquor</h2>
  <h3 class="section-title" style="left:16px;top:48px;font-size:8px">Vodka</h3>
  <ul class="items" style="left:16px;top:59px;width:60px"><li><span>Well Vodka</span><b>7</b></li><li><span>Citrus Vodka</span><b>8</b></li><li><span>Premium Vodka</span><b>10</b></li><li><span>Rice Vodka</span><b>9</b></li></ul>
  <h3 class="section-title" style="left:86px;top:48px;font-size:8px">Gin</h3>
  <ul class="items" style="left:86px;top:59px;width:60px"><li><span>Well Gin</span><b>7</b></li><li><span>Dry Gin</span><b>9</b></li><li><span>Botanical Gin</span><b>10</b></li></ul>
  <h3 class="section-title" style="left:156px;top:48px;font-size:8px">Rum</h3>
  <ul class="items" style="left:156px;top:59px;width:60px"><li><span>White Rum</span><b>7</b></li><li><span>Gold Rum</span><b>8</b></li><li><span>Dark Rum</span><b>9</b></li><li><span>Spiced Rum</span><b>8</b></li></ul>
  <h3 class="section-title" style="left:16px;top:104px;font-size:8px">Tequila</h3>
  <ul class="items" style="left:16px;top:115px;width:60px"><li><span>Well Tequila</span><b>7</b></li><li><span>Blanco Tequila</span><b>9</b></li><li><span>Reposado Pour</span><b>11</b></li><li><span>Añejo Pour</span><b>13</b></li></ul>
  <h3 class="section-title" style="left:86px;top:104px;font-size:8px">Whiskey</h3>
  <ul class="items" style="left:86px;top:115px;width:60px"><li><span>Well Whiskey</span><b>7</b></li><li><span>Rye Whiskey</span><b>10</b></li><li><span>Irish Whiskey</span><b>10</b></li><li><span>Japanese Whisky</span><b>14</b></li></ul>
  <h3 class="section-title" style="left:156px;top:104px;font-size:8px">Scotch</h3>
  <ul class="items" style="left:156px;top:115px;width:60px"><li><span>Blended Scotch</span><b>10</b></li><li><span>Single Malt</span><b>14</b></li><li><span>Aged Malt</span><b>18</b></li></ul>
  <h3 class="section-title" style="left:86px;top:160px;font-size:8px">Brandy</h3>
  <ul class="items" style="left:86px;top:171px;width:60px"><li><span>House Brandy</span><b>9</b></li><li><span>Fine Cognac</span><b>14</b></li><li><span>Aged Cognac</span><b>18</b></li></ul>
  <div class="abs" role="img" aria-label="Iced cocktail with lime" style="left:14px;top:200px;width:56px;height:110px;background:linear-gradient(180deg,#eef6e2,#b8d98a 60%,#6f9a3a)"></div>
  <h2 class="section-title section-title--red" style="left:16px;top:330px;font-size:18px">Cocktails</h2>
  <ul class="items" style="left:16px;top:356px;width:112px">
    <li><span>Mai Tai</span><b>12</b></li><li><span>Lychee Martini</span><b>13</b></li><li><span>Mojito</span><b>11</b></li><li><span>Margarita</span><b>11</b></li><li><span>Old Fashioned</span><b>13</b></li><li><span>Cosmopolitan</span><b>12</b></li><li><span>Tokyo Mule</span><b>12</b></li><li><span>Sake Sangria</span><b>11</b></li>
  </ul>
  <div class="abs" role="img" aria-label="Fresh lemons and citrus slices" style="left:138px;top:380px;width:94px;height:203px;background:linear-gradient(160deg,#fefaee,#fae287 40%,#f8cf3a 70%,#d9a520)"></div>
</section>

</body>
</html>
```